Customs House descriptive business cards

We require a two-sided business card that has a simple yet elegant design. We want to be able to promote our services as a customs house. This card should include our logo, contact info and services offered with the logo being on one side and the contact info and services on the flip side

Target Market(s)

Importers / exporters to and from the Bahamas

Industry/Entity Type

Logistics

Contact Information for Business Card

The front side of the card could have the logo and the flip side should have the other relevant info

Font styles to use
Serif

Colors

Designer to choose colors to be used in the design.

Requirements
Must have
• (Harbourline Agents Ltd) Logo, address and contact info also services:
• import customs clearance, Delivery & HAndling services,Florida pickups, Export packing & Crating Services, export customs clearance, Consulting

```html
<!DOCTYPE html>
<html lang="en">
<head>
<meta charset="utf-8">
<title>Harbourline Agents Ltd – Business Card</title>
<link rel="stylesheet" href="https://fonts.googleapis.com/css2?family=EB+Garamond:wght@400;500&display=swap">
<style>
  :root {
    --backdrop: #232323;
    --card: #1c1c1d;
    --card-edge: #2a2a2b;
    --brand-blue: #2a86d6;
    --silver: #9a9a9a;
    --silver-light: #d8d8d8;
    --ink: #f2f2f2;
    --muted: #cfcfcf;
  }
  * { margin: 0; padding: 0; box-sizing: border-box; }
  html, body {
    width: 1200px;
    height: 900px;
    overflow: hidden;
    background: var(--backdrop);
    font-family: "EB Garamond", Georgia, serif;
  }
  .canvas { position: relative; width: 1200px; height: 900px; }
  .card {
    position: absolute;
    left: 250px;
    width: 700px;
    height: 400px;
    background: var(--card);
    border: 1px solid var(--card-edge);
    overflow: hidden;
  }
  .card--front { top: 35px; }
  .card--back  { top: 465px; }

  /* Front */
  .front-mark {
    position: absolute;
    left: 50%;
    top: 110px;
    transform: translateX(-50%);
    display: flex;
    flex-direction: column;
    align-items: center;
    gap: 22px;
  }
  .front-mark__dot {
    width: 70px;
    height: 70px;
    border-radius: 50%;
    background: var(--silver);
  }
  .front-mark__name {
    font-weight: 500;
    font-size: 34px;
    letter-spacing: 2px;
    text-transform: uppercase;
    color: var(--silver);
    white-space: nowrap;
  }

  /* Back */
  .back-brand {
    position: absolute;
    left: 50px;
    top: 40px;
    font-weight: 500;
    font-size: 34px;
    letter-spacing: 1px;
    text-transform: uppercase;
    color: var(--brand-blue);
    line-height: 1.05;
  }
  .contact {
    position: absolute;
    left: 60px;
    top: 150px;
    color: var(--ink);
    font-size: 18px;
    line-height: 1.35;
  }
  .contact__name {
    font-size: 22px;
    letter-spacing: 2px;
    text-transform: uppercase;
    color: var(--brand-blue);
  }
  .contact__role { font-size: 16px; margin-bottom: 14px; color: var(--muted); }
  .contact__address { margin-bottom: 10px; }
  .contact__row {
    display: flex;
    align-items: center;
    gap: 10px;
    margin-top: 4px;
  }
  .contact__row svg { flex: none; }
  .contact__domain { color: var(--brand-blue); }

  .back-accent {
    position: absolute;
    right: 70px;
    top: 40px;
    width: 150px;
    height: 150px;
    border-radius: 50%;
    background: linear-gradient(135deg, #3a3a3a 0%, var(--silver-light) 100%);
  }
  .services {
    position: absolute;
    left: 430px;
    top: 212px;
    width: 240px;
    color: var(--ink);
  }
  .services__title {
    font-size: 16px;
    letter-spacing: 2px;
    text-transform: uppercase;
    color: var(--brand-blue);
    margin-bottom: 6px;
  }
  .services__list {
    list-style: none;
    font-size: 15px;
    line-height: 1.3;
  }
  .services__list li::before {
    content: "";
    display: inline-block;
    width: 5px;
    height: 5px;
    margin: 0 8px 3px 0;
    background: var(--brand-blue);
  }
</style>
</head>
<body>
<main class="canvas">
  <section class="card card--front" aria-label="Card front">
    <div class="front-mark">
      <span class="front-mark__dot"></span>
      <span class="front-mark__name">Harbourline Agents Ltd</span>
    </div>
  </section>

  <section class="card card--back" aria-label="Card back">
    <div class="back-brand">Harbourline<br>Agents Ltd</div>
    <div class="contact">
      <p class="contact__name">Daniel Roberts</p>
      <p class="contact__role">Director</p>
      <p class="contact__address">215 Harbor View Rd Suite 12<br>Tampa, Florida, 33602</p>
      <p class="contact__row">
        <svg width="12" height="14" viewBox="0 0 12 14"><path d="M3 1 L5 4 L3.5 5.5 Q5 9 8 10.5 L9.5 9 L12 11 L10 13.5 Q3 12 0.5 3 Z" fill="var(--brand-blue)"/></svg>
        555.210.4837
      </p>
      <p class="contact__row">
        <svg width="14" height="10" viewBox="0 0 14 10"><rect x="0.75" y="0.75" width="12.5" height="8.5" fill="none" stroke="var(--brand-blue)" stroke-width="1.5"/><path d="M1 1 L7 6 L13 1" fill="none" stroke="var(--brand-blue)" stroke-width="1.5"/></svg>
        info@harbourlineagents.com
      </p>
      <p class="contact__row">
        <svg width="14" height="14" viewBox="0 0 14 14"><circle cx="7" cy="7" r="6" fill="none" stroke="var(--brand-blue)" stroke-width="1.3"/><path d="M1 7 H13 M7 1 Q3 7 7 13 M7 1 Q11 7 7 13" fill="none" stroke="var(--brand-blue)" stroke-width="1"/></svg>
        <span>www.<span class="contact__domain">harbourlineagents</span>.com</span>
      </p>
    </div>
    <span class="back-accent"></span>
    <div class="services">
      <p class="services__title">Services</p>
      <ul class="services__list">
        <li>Import Customs Clearance</li>
        <li>Delivery &amp; Handling Services</li>
        <li>Florida Pickups</li>
        <li>Export Packing &amp; Crating</li>
        <li>Export Customs Clearance</li>
        <li>Consulting</li>
      </ul>
    </div>
  </section>
</main>
</body>
</html>
```